4Orbit Blueprint- Logo & Design Work

THIS IS PHASE ONE. I have a stock trading strategy. I need a schematic that shows how it works. I have included sketches. I want the scheme to look like Exhibit A. I want the circles to look like gear shifts in Exhibit B. After this first step is done, we will move on to creating logo like Exhibit C, a second logo like Exhibit D and another Schematic like Exhibit E.

```html
<!DOCTYPE html>
<html lang="en">
<head>
<meta charset="utf-8">
<title>4Orbit Blueprint – Strategy Schematic</title>
<link href="https://fonts.googleapis.com/css2?family=Open+Sans:wght@700&display=swap" rel="stylesheet">
<style>
  :root {
    --bg: #ffffff;
    --green-dark: #178a3f;
    --green-mid: #2a9a42;
    --green-light: #3aa843;
    --blue-dark: #1c5fa8;
    --blue-light: #2aa6d2;
    --text: #ffffff;
  }
  html, body {
    margin: 0;
    padding: 0;
    overflow: hidden;
    background: var(--bg);
  }
  .schematic {
    position: relative;
    width: 1200px;
    height: 927px;
    background: var(--bg);
    overflow: hidden;
    font-family: "Open Sans", Arial, sans-serif;
  }
  .schematic-art {
    position: absolute;
    inset: 0;
  }
  .gear-label {
    position: absolute;
    width: 130px;
    margin-left: -65px;
    text-align: center;
    color: var(--text);
    font-weight: 700;
    font-size: 17px;
    line-height: 20px;
    transform: translateY(-50%);
  }
  .gear-label .note {
    display: block;
    font-size: 8.5px;
    line-height: 11px;
    margin-top: 4px;
  }
</style>
</head>
<body>
<div class="schematic">
  <svg class="schematic-art" width="1200" height="927" viewBox="0 0 1200 927" xmlns="http://www.w3.org/2000/svg">
    <defs>
      <radialGradient id="gear-fill" cx="0" cy="0" r="100" gradientUnits="userSpaceOnUse">
        <stop offset="0.6" stop-color="var(--green-dark)"/>
        <stop offset="0.8" stop-color="var(--green-light)"/>
        <stop offset="1" stop-color="var(--green-mid)"/>
      </radialGradient>
      <linearGradient id="bar-h" x1="0" x2="1" y1="0" y2="0">
        <stop offset="0" stop-color="var(--green-dark)"/>
        <stop offset="0.5" stop-color="var(--green-light)"/>
        <stop offset="1" stop-color="var(--green-dark)"/>
      </linearGradient>
      <linearGradient id="bar-v" x1="0" x2="0" y1="0" y2="1">
        <stop offset="0" stop-color="var(--green-dark)"/>
        <stop offset="0.5" stop-color="var(--green-light)"/>
        <stop offset="1" stop-color="var(--green-dark)"/>
      </linearGradient>
      <radialGradient id="arrow-fill" cx="100" cy="0" r="80" gradientUnits="userSpaceOnUse">
        <stop offset="0" stop-color="var(--blue-light)"/>
        <stop offset="1" stop-color="var(--blue-dark)"/>
      </radialGradient>
      <polygon id="tooth" points="-13,-99 13,-99 17,-78 -17,-78"/>
      <g id="gear">
        <g fill="url(#gear-fill)">
          <circle r="86"/>
          <use href="#tooth"/>
          <use href="#tooth" transform="rotate(30)"/>
          <use href="#tooth" transform="rotate(60)"/>
          <use href="#tooth" transform="rotate(90)"/>
          <use href="#tooth" transform="rotate(120)"/>
          <use href="#tooth" transform="rotate(150)"/>
          <use href="#tooth" transform="rotate(180)"/>
          <use href="#tooth" transform="rotate(210)"/>
          <use href="#tooth" transform="rotate(240)"/>
          <use href="#tooth" transform="rotate(270)"/>
          <use href="#tooth" transform="rotate(300)"/>
          <use href="#tooth" transform="rotate(330)"/>
        </g>
        <circle r="68" fill="var(--green-dark)" stroke="#ffffff" stroke-width="1.8"/>
      </g>
      <polygon id="arrow" fill="url(#arrow-fill)" points="0,-12 92,-12 92,-33 142,0 92,33 92,12 0,12"/>
    </defs>

    <g class="connectors">
      <rect x="449" y="211" width="301" height="19" fill="url(#bar-h)"/>
      <rect x="449" y="695" width="301" height="19" fill="url(#bar-h)"/>
      <rect x="337" y="326" width="19" height="275" fill="url(#bar-v)"/>
      <rect x="844" y="326" width="19" height="276" fill="url(#bar-v)"/>
    </g>

    <g class="gears">
      <use href="#gear" transform="translate(346 223)"/>
      <use href="#gear" transform="translate(854 223)"/>
      <use href="#gear" transform="translate(346 704)"/>
      <use href="#gear" transform="translate(854 704)"/>
      <use href="#gear" transform="translate(600 463)"/>
    </g>

    <g class="flow-arrows">
      <use href="#arrow" transform="translate(420 294) rotate(42)"/>
      <use href="#arrow" transform="translate(780 294) rotate(138)"/>
      <use href="#arrow" transform="translate(420 633) rotate(-42)"/>
      <use href="#arrow" transform="translate(780 633) rotate(-138)"/>
    </g>
  </svg>

  <div class="gear-label" style="left:345px; top:226px;">Rebalance<br>Annually<span class="note">LOREN IPSUM<br>LOREN</span></div>
  <div class="gear-label" style="left:854px; top:221px;">Trend<br>33%<br>Allocation</div>
  <div class="gear-label" style="left:346px; top:703px;">Buy &amp; Hold<br>33%<br>Allocation</div>
  <div class="gear-label" style="left:854px; top:703px;">Tactical<br>33%<br>Allocation</div>
  <div class="gear-label" style="left:600px; top:462px;">4Orbit<br>World Stock<br>Index<br>Blueprint</div>
</div>
</body>
</html>
```